Expedited Project Word Template, envelopes and powerpoint template
no business card needed already have
n/a
2486 Quill Basin Lane
Brenford, OH 44190
info@tivelmora.com
-uploaded logo needs to have ® symbol placed after the word "growing"
-already have business cards just need word template and letterhead and envelopes
-business focused on renewable energies/fresh produce production/environment, looking for classic corporate look
--trying to limit cost of printing as a start-up, so preference is for white background and then use color to highlight key areas
--powerpoint template looking for title slide, section break slide, main content slide, table slide, and image slide. template should include page numbering and private/confidential in the footer.
Here is how my biz card looks -- please note the tag line on this copy is correct"
"where craft and field align"

```html
<!DOCTYPE html>
<html lang="en">
<head>
<meta charset="UTF-8">
<title>Tivelmora Halden – Stationery</title>
<link rel="stylesheet" href="https://fonts.googleapis.com/css2?family=Montserrat:wght@400;500;600;700&display=swap">
<style>
  :root {
    --olive: #4e4b24;
    --leaf: #8cc63f;
    --sky: #2aa8d8;
    --paper: #ffffff;
    --backdrop: #eceef0;
    --rule: #c9cbc4;
    --ink: #55584a;
    --header-ink: #f3f3ea;
  }
  * { box-sizing: border-box; margin: 0; padding: 0; }
  html, body { width: 1200px; height: 768px; overflow: hidden; }
  body {
    background: var(--backdrop);
    font-family: "Montserrat", Arial, sans-serif;
    color: var(--ink);
    position: relative;
  }
  .sheet {
    position: absolute;
    top: 164px;
    width: 340px;
    height: 440px;
    background: var(--paper);
    box-shadow: 0 2px 10px rgba(0,0,0,0.18);
  }
  .letterhead { left: 40px; }
  .second-sheet { left: 410px; }
  .sheet-header {
    height: 74px;
    background: var(--olive);
    position: relative;
  }
  .brand {
    position: absolute;
    left: 16px;
    bottom: 12px;
    display: flex;
    flex-direction: column;
    gap: 3px;
  }
  .brand-row { display: flex; align-items: center; gap: 6px; }
  .brand-dot {
    width: 12px; height: 12px; border-radius: 50%;
    background: var(--sky);
    flex: none;
  }
  .brand-name {
    font-size: 8.5px;
    font-weight: 700;
    letter-spacing: 0.6px;
    color: var(--leaf);
    text-transform: uppercase;
    white-space: nowrap;
  }
  .brand-tagline {
    font-size: 5px;
    color: var(--header-ink);
    letter-spacing: 0.3px;
    padding-left: 18px;
    white-space: nowrap;
  }
  .contact {
    position: absolute;
    left: 196px;
    top: 10px;
    font-size: 6px;
    line-height: 9px;
    color: var(--header-ink);
    white-space: nowrap;
  }
  .contact .gap { height: 5px; }
  .contact-line { display: flex; align-items: center; gap: 4px; }
  .contact-line svg { width: 7px; height: 7px; }
  .second-sheet .contact { left: 118px; }
  .notes-box {
    position: absolute;
    left: 18px;
    top: 98px;
    width: 120px;
    height: 150px;
    border: 1px solid var(--rule);
    padding: 10px 10px;
    display: flex;
    flex-direction: column;
    gap: 17px;
  }
  .notes-box span { display: block; border-bottom: 1px solid var(--rule); }
  .envelope {
    position: absolute;
    left: 780px;
    top: 301px;
    width: 380px;
    height: 165px;
    background: var(--paper);
    box-shadow: 0 2px 10px rgba(0,0,0,0.18);
    overflow: hidden;
  }
  .envelope-flap { position: absolute; left: 0; top: 0; width: 380px; height: 70px; }
  .envelope .brand { left: 16px; bottom: auto; top: 78px; }
  .envelope .brand-tagline { color: var(--ink); }
  .return-address {
    position: absolute;
    left: 16px;
    bottom: 14px;
    font-size: 6.5px;
    line-height: 9px;
    font-style: normal;
    color: var(--ink);
  }
</style>
</head>
<body>
  <section class="sheet letterhead" aria-label="Letterhead">
    <header class="sheet-header">
      <div class="brand">
        <div class="brand-row">
          <span class="brand-dot"></span>
          <span class="brand-name">Tivelmora Halden</span>
        </div>
        <span class="brand-tagline">where craft and field align</span>
      </div>
      <div class="contact">
        <div>2486 Quill Basin Lane</div>
        <div>Brenford, OH 44190</div>
        <div class="gap"></div>
        <div class="contact-line">
          <svg viewBox="0 0 10 10"><path d="M2 1h2l1 2-1 1c.6 1.2 1.4 2 2.6 2.6l1-1 2 1v2c0 .5-.5 1-1 1C4.5 9.6.4 5.5 1 2c0-.5.5-1 1-1z" fill="currentColor"/></svg>
          <span>419-555-0162</span>
        </div>
        <div class="contact-line">
          <svg viewBox="0 0 10 10"><rect x="1" y="2" width="8" height="6" fill="none" stroke="currentColor"/><path d="M1 2l4 3 4-3" fill="none" stroke="currentColor"/></svg>
          <span>info@tivelmora.com</span>
        </div>
      </div>
    </header>
  </section>

  <section class="sheet second-sheet" aria-label="Second page">
    <header class="sheet-header">
      <div class="contact">
        <div>2486 Quill Basin Lane</div>
        <div>Brenford, OH 44190</div>
        <div class="gap"></div>
        <div class="contact-line">
          <svg viewBox="0 0 10 10"><path d="M2 1h2l1 2-1 1c.6 1.2 1.4 2 2.6 2.6l1-1 2 1v2c0 .5-.5 1-1 1C4.5 9.6.4 5.5 1 2c0-.5.5-1 1-1z" fill="currentColor"/></svg>
          <span>419-555-0162</span>
        </div>
        <div class="contact-line">
          <svg viewBox="0 0 10 10"><rect x="1" y="2" width="8" height="6" fill="none" stroke="currentColor"/><path d="M1 2l4 3 4-3" fill="none" stroke="currentColor"/></svg>
          <span>info@tivelmora.com</span>
        </div>
      </div>
    </header>
    <div class="notes-box"><span></span><span></span><span></span><span></span><span></span><span></span></div>
  </section>

  <section class="envelope" aria-label="Envelope">
    <svg class="envelope-flap" viewBox="0 0 380 70" preserveAspectRatio="none">
      <path d="M0 0H380V44C300 70 240 60 190 52 130 42 60 44 0 66Z" fill="var(--olive)"/>
    </svg>
    <div class="brand">
      <div class="brand-row">
        <span class="brand-dot"></span>
        <span class="brand-name">Tivelmora Halden</span>
      </div>
      <span class="brand-tagline">where craft and field align</span>
    </div>
    <address class="return-address">
      <div>2486 Quill Basin Lane</div>
      <div>Brenford, OH 44190</div>
    </address>
  </section>
</body>
</html>
```